Jewelry Back Card Graphic Design

I am looking for a graphic design to print out and put in the back of the jewelry box for my long-distance jewelry. I attached an example that I am now using for the "still harbor jewelry" so you can see what it's used for.

But this card needs to relate to people who are in a long-distance relationship or friendship, so it needs to resonate with them when they see it on the website and open the box if they receive the jewelry as a gift.

I attached a rough idea that I sketched myself, but you can be creative and create anything else if you have a better idea.

It needs to be square.

Looking forward to the results!

```html
<!DOCTYPE html>
<html lang="en">
<head>
<meta charset="utf-8">
<title>Long-Distance Jewelry Back Card</title>
<link rel="stylesheet" href="https://fonts.googleapis.com/css2?family=Satisfy&display=swap">
<style>
  :root {
    --page-bg: #ffffff;
    --sky-top: #5a1f3a;
    --sky-mid: #c8361f;
    --sky-glow: #f7a21e;
    --ridge: #8a2a36;
    --sea-dark: #1f1d33;
    --sea-mid: #3a2d45;
    --shore-glow: #e8621a;
    --sand-dark: #3b1a14;
    --message: #ffffff;
    --message-shadow: rgba(20, 10, 25, 0.85);
  }
  * { margin: 0; padding: 0; box-sizing: border-box; }
  html, body {
    width: 1200px;
    height: 1200px;
    overflow: hidden;
    background: var(--page-bg);
  }
  .back-card {
    position: relative;
    width: 1200px;
    height: 1200px;
  }
  .sunset-scene {
    position: absolute;
    inset: 0;
    background: linear-gradient(
      to bottom,
      var(--sky-top) 0%,
      var(--sky-mid) 18%,
      var(--sky-glow) 36%,
      var(--ridge) 46%,
      var(--sea-dark) 49%,
      var(--sea-mid) 62%,
      var(--shore-glow) 78%,
      var(--sand-dark) 100%
    );
  }
  .card-message {
    position: absolute;
    left: 0;
    right: 0;
    top: 605px;
    text-align: center;
    font-family: "Satisfy", cursive;
    font-size: 78px;
    line-height: 1.25;
    color: var(--message);
    text-shadow: 0 2px 6px var(--message-shadow);
    letter-spacing: 1px;
  }
</style>
</head>
<body>
  <main class="back-card">
    <div class="sunset-scene" role="img" aria-label="Illustrated sunset over the sea: fiery red and orange clouds, a glowing sun setting between mountains, waves rolling onto a beach lit by golden reflections"></div>
    <p class="card-message">A True Connection<br>Goes Beyond Horizont</p>
  </main>
</body>
</html>
```